Linden Medical - Flyer

We are a full service pharmacy that specializes in diabetic testing and medications. We research the patient's insurance to maximize their insurance benefit and then deliver the medications monthly directly to the patient's doorstep, for free! We save the patient, time and money every month.
We would love a flyer that we can distribute to Doctor's offices and patients that sum up our pharmacy. Emphasis on saving money, time, and getting the best quality supplies by maximizing their insurance. We want it to be eye catching, clean, and professional.
You can use our logo or feel free to make your own design.
Updates
Target Market(s)
diabetic patients wanting to save money
Industry/Entity Type
Insurance
Look and feel
Each slider illustrates characteristics of the customer's brand and the style your logo design should communicate.

```html
<!DOCTYPE html>
<html lang="en">
<head>
<meta charset="utf-8">
<title>Linden Medical – Flyer</title>
<link rel="stylesheet" href="https://fonts.googleapis.com/css2?family=Open+Sans:wght@600;700&display=swap">
<style>
  :root {
    --white: #ffffff;
    --swoosh-grey: #c9cdd0;
    --leaf-green: #6aa313;
    --leaf-green-dark: #4f8a0a;
    --navy: #070a4a;
    --navy-deep: #03053a;
    --gold: #e3aa1c;
    --mint: #d5f2d6;
    --ink-dark: #10153d;
    --panel-top: #0a1a8c;
    --panel-bottom: #050e5e;
    --panel-edge: #4a62d8;
    --photo-light: #f4f5f7;
    --photo-mid: #d9dde2;
  }
  * { margin: 0; padding: 0; box-sizing: border-box; }
  html, body { width: 1200px; height: 2545px; overflow: hidden; }
  body { font-family: "Open Sans", Arial, sans-serif; background: var(--white); }
  .flyer { position: relative; width: 1200px; height: 2545px; background: var(--navy); overflow: hidden; }

  .masthead { position: absolute; left: 0; top: 0; width: 1200px; height: 470px; background: var(--white); }
  .brand { position: absolute; left: 0; top: 175px; width: 1200px; display: flex; justify-content: center; align-items: center; gap: 34px; }
  .brand-dot { width: 96px; height: 96px; border-radius: 50%; background: var(--leaf-green); }
  .brand-name { font-size: 98px; font-weight: 700; line-height: 1; color: var(--navy); }

  .band-art { position: absolute; left: 0; top: 410px; width: 1200px; height: 200px; }
  .about-title { position: absolute; left: 0; top: 488px; width: 1200px; text-align: center; font-weight: 700; font-size: 64px; line-height: 88px; color: var(--ink-dark); text-shadow: 2px 3px 3px rgba(0,0,0,0.35); }

  .about { position: absolute; left: 0; top: 586px; width: 1200px; height: 504px; background: linear-gradient(180deg, var(--navy) 0%, var(--navy-deep) 100%); padding: 24px 0 0 30px; }
  .about p { color: var(--gold); font-weight: 600; font-size: 42px; line-height: 56px; white-space: nowrap; }
  .about p + p { margin-top: 56px; }

  .photo { position: absolute; left: 0; top: 1090px; width: 1200px; height: 745px; background: radial-gradient(ellipse at 45% 55%, var(--photo-light) 0%, var(--photo-mid) 100%); }

  .savings { position: absolute; left: 0; top: 1835px; width: 1200px; height: 710px; background: linear-gradient(180deg, var(--navy-deep) 0%, var(--navy) 100%); }
  .savings-title, .savings-footer { position: absolute; left: 0; width: 1200px; text-align: center; font-weight: 700; font-size: 70px; line-height: 96px; color: var(--mint); text-shadow: 2px 4px 4px rgba(0,0,0,0.6); }
  .savings-title { top: 60px; }
  .savings-footer { top: 575px; }
  .panels { position: absolute; left: 0; top: 249px; width: 1200px; height: 265px; }
  .panel-label { position: absolute; text-align: center; font-weight: 700; color: var(--gold); text-shadow: 0 10px 4px rgba(0,0,0,0.7); line-height: 1.05; }
  .label-patient { left: 13px; width: 344px; top: 45px; font-size: 66px; }
  .label-time { left: 408px; width: 402px; top: 76px; font-size: 96px; }
  .label-money { left: 828px; width: 359px; top: 92px; font-size: 70px; }
</style>
</head>
<body>
<main class="flyer">
  <header class="masthead">
    <div class="brand">
      <span class="brand-dot" aria-hidden="true"></span>
      <span class="brand-name">Linden Medical</span>
    </div>
  </header>

  <svg class="band-art" viewBox="0 0 1200 200" aria-hidden="true">
    <path d="M0 30 Q600 -20 1200 45 L1200 70 Q600 10 0 60 Z" fill="var(--swoosh-grey)"/>
    <path d="M0 60 Q600 10 1200 70 L1200 176 L0 176 Z" fill="var(--leaf-green)"/>
    <rect x="0" y="165" width="1200" height="11" fill="var(--leaf-green-dark)"/>
  </svg>
  <h2 class="about-title">ABOUT US:</h2>

  <section class="about">
    <p>&nbsp;We are a full service pharmacy that specializes<br>in diabetic testing and medications.</p>
    <p>&nbsp;We research the patient's insurance to maxi-<br>mize their insurance benefit and then deliver the<br>medications monthly directly to the patient's<br>doorstep, for free!</p>
  </section>

  <div class="photo" role="img" aria-label="Photo of an orange prescription bottle tipped over with white tablets spilling out beside its cap"></div>

  <section class="savings">
    <h2 class="savings-title">WE SAVE:</h2>
    <div class="panels">
      <svg width="1200" height="265" viewBox="0 0 1200 265" aria-hidden="true">
        <defs>
          <linearGradient id="panelFill" x1="0" y1="0" x2="0" y2="1">
            <stop offset="0" stop-color="var(--panel-top)"/>
            <stop offset="1" stop-color="var(--panel-bottom)"/>
          </linearGradient>
        </defs>
        <g fill="url(#panelFill)" stroke="var(--panel-edge)" stroke-width="3">
          <polygon points="38,0 344,0 357,265 13,265"/>
          <polygon points="446,0 764,0 810,265 408,265"/>
          <polygon points="879,0 1159,0 1187,265 828,265"/>
        </g>
      </svg>
      <span class="panel-label label-patient">The<br>Patient</span>
      <span class="panel-label label-time">TIME</span>
      <span class="panel-label label-money">Money</span>
    </div>
    <p class="savings-footer">Every Month</p>
  </section>
</main>
</body>
</html>
```